TLR Property - Business Cards

Looking for a business card & general letterhead, signage etc design for our new logo.

Colours:
000a20
0056a2
00b5ef
0088ce
68cef2

Fonts:
Poppins
Karla

Please keep look and feel of new brand - example in the zip package I sent.

```html
<!DOCTYPE html>
<html lang="en">
<head>
<meta charset="utf-8">
<title>TLR Property – Business Cards</title>
<link rel="stylesheet" href="https://fonts.googleapis.com/css2?family=Poppins:wght@400;500;700&display=swap">
<style>
  :root {
    --navy: #0a0f1e;
    --ink: #000a20;
    --brand-blue: #0056a2;
    --sky: #00b5ef;
    --mid-blue: #0088ce;
    --pale-blue: #68cef2;
    --text-light: #e8ecf3;
    --backdrop: #d9dce1;
  }
  * { margin: 0; padding: 0; box-sizing: border-box; }
  html, body { width: 1200px; height: 900px; overflow: hidden; }
  body {
    background: var(--backdrop);
    font-family: "Poppins", sans-serif;
    display: flex;
    flex-direction: column;
    align-items: center;
    justify-content: center;
    gap: 60px;
  }
  .card {
    position: relative;
    width: 630px;
    height: 360px;
    border-radius: 26px;
    background: var(--navy);
    overflow: hidden;
    box-shadow: 0 10px 30px rgba(0, 10, 32, 0.25);
  }
  .card-swoosh { position: absolute; left: 0; bottom: 0; width: 100%; height: 100%; }
  .wordmark {
    font-family: "Poppins", sans-serif;
    font-weight: 700;
    color: var(--brand-blue);
    letter-spacing: 2px;
    line-height: 1;
  }
  .card-front .wordmark {
    position: absolute;
    left: 60px;
    top: 95px;
    font-size: 76px;
  }
  .card-front .divider {
    position: absolute;
    left: 300px;
    top: 70px;
    width: 2px;
    height: 170px;
    background: var(--mid-blue);
    transform: skewX(-20deg);
  }
  .contact {
    position: absolute;
    left: 335px;
    top: 72px;
    color: var(--text-light);
    font-size: 15px;
    line-height: 1.45;
  }
  .contact-name {
    color: var(--brand-blue);
    font-weight: 700;
    font-size: 21px;
    text-transform: uppercase;
    letter-spacing: 0.5px;
    line-height: 1.1;
  }
  .contact-role { font-size: 15px; margin-bottom: 10px; }
  .contact-address { margin-bottom: 8px; }
  .contact-line { display: flex; align-items: center; gap: 8px; }
  .contact-line svg { width: 13px; height: 13px; flex: none; }
  .card-back { display: flex; align-items: center; justify-content: center; }
  .card-back .wordmark { font-size: 150px; letter-spacing: 6px; }
</style>
</head>
<body>

<section class="card card-front" aria-label="Business card front">
  <svg class="card-swoosh" viewBox="0 0 630 360" preserveAspectRatio="none" aria-hidden="true">
    <path d="M0 235 C 120 300, 330 340, 630 318 L630 360 L0 360 Z" fill="var(--sky)"/>
    <path d="M0 250 C 140 318, 340 350, 630 336 L630 360 L0 360 Z" fill="var(--mid-blue)"/>
    <path d="M0 215 C 150 300, 360 332, 630 322" fill="none" stroke="var(--sky)" stroke-width="2"/>
  </svg>

  <div class="wordmark">TLR</div>
  <div class="divider"></div>

  <div class="contact">
    <p class="contact-name">Daniel Hart</p>
    <p class="contact-role">Managing Director</p>
    <p class="contact-address">Your address, City<br>state, Zip 1234</p>
    <p class="contact-line">
      <svg viewBox="0 0 16 16"><path d="M4 1 L6.5 1 L7.5 5 L5.5 6.3 C6.5 8.4 7.6 9.5 9.7 10.5 L11 8.5 L15 9.5 L15 12 C15 13.7 13.7 15 12 15 C6 15 1 10 1 4 C1 2.3 2.3 1 4 1 Z" fill="var(--sky)"/></svg>
      555 318 204
    </p>
    <p class="contact-line">
      <svg viewBox="0 0 16 16"><rect x="1" y="3" width="14" height="10" rx="1.5" fill="var(--sky)"/><path d="M1.5 4 L8 9 L14.5 4" fill="none" stroke="var(--navy)" stroke-width="1.3"/></svg>
      hello@tlrproperty.com
    </p>
    <p class="contact-line">
      <svg viewBox="0 0 16 16"><circle cx="8" cy="8" r="7" fill="var(--sky)"/><path d="M1 8 H15 M8 1 C5 4 5 12 8 15 C11 12 11 4 8 1" fill="none" stroke="var(--navy)" stroke-width="1.1"/></svg>
      www.tlrproperty.com
    </p>
  </div>
</section>

<section class="card card-back" aria-label="Business card back">
  <div class="wordmark">TLR</div>
</section>

</body>
</html>
```